Pell Hartwick - Magazine

Our client would like a magazine designed for a conceptual novelty based on unconventional views on contemporary issues, including; finance, religion, politics etc.!

The novelty includes 1 main article, supporting images and 12 short poems.
We would like the designer to create page vectors, borders, fonts and other layout design elements.

In the first stage of the competition we request:

Magazine layout - 6 pages( 4 article variations based on article content and 2 poem page designs)

We would like to see high impact, striking vectors and design concepts to compliment the article content. See attached bullet point guide to article to help design page themes.

COMPANY INFO
Writer, poet, researcher and commentator. Our client is interested in sharing art and issues he believes in. Our client would like to design one magazine issue first but has a collection of material to produce a series of magazines in the future. So he is looking to establish a potentially long-term partnership with designer(s).

Target Market(s)

Quick and easy to read, coffee time magazine. Target Market: Male 40yrs+, Intellectual, Open Minded.

Industry/Entity Type

Finance

Font styles to use
Serif
Decorative

Requirements
Must have
• Main Article and Poetry: Space for 1 -2 images per page.
A subtle design feature that connects each page.
Primary colors: Jade Green and some Grayscale.
Secondary Colors: 3rd and 4th color open to designers preference.
Page Dimensions : 7.5in height, 7in width.
Articles: Same color theme, different layout and vector choice, same font color and size.
Poetry: Some design creative freedom. Focus on creating a unique title font incorporating the theme of the poem, Poetry TITLE font must be made a feature design element (poem identity)
Font: See Veldtrove Quarterly magazine styling
Columns: Single or multiple.
All vectors and images should be sourced from pixel quarry.
Nice to have
• Images/pictures that connect with article topic and align with color theme.
Should not have
• Avoid repetition of page design. To do this follow the idea of each paragraph (see attached breakdown)

```html
<!DOCTYPE html>
<html lang="en">
<head>
<meta charset="utf-8">
<title>Vested Vermin from a Jade Terrace – Spread</title>
<link rel="stylesheet" href="https://fonts.googleapis.com/css2?family=Arimo:ital,wght@0,400;0,700;1,400&family=Open+Sans:wght@700;800&display=swap">
<style>
  :root {
    --backdrop: #f4f4f4;
    --page: #efefef;
    --page-light: #f8f8f8;
    --ink: #4a4a4a;
    --ink-soft: #6c6c6c;
    --title-grey: #6a6a6a;
    --wall-dark: #9a9a9a;
    --wall-mid: #d2d2d2;
    --sign-white: #f7f7f7;
    --sign-edge: #8a8a8a;
    --sign-ink: #111111;
    --caduceus-blue: #5d6f8f;
    --badge: #3e3e3e;
  }
  * { box-sizing: border-box; margin: 0; padding: 0; }
  html, body { width: 1200px; height: 1000px; overflow: hidden; }
  body { background: var(--backdrop); position: relative; font-family: "Arimo", Arial, sans-serif; }

  .spread {
    position: absolute; left: 40px; top: 240px; width: 1120px; height: 522px;
    background: linear-gradient(90deg, var(--page) 0%, var(--page-light) 50%, var(--page) 100%);
    overflow: hidden;
  }

  /* left page: quotation sign on a wall */
  .quote-wall {
    position: absolute; left: 0; top: 0; width: 520px; height: 522px; overflow: hidden;
    background: linear-gradient(160deg, var(--wall-dark) 0%, var(--wall-mid) 40%, #e6e6e6 75%, var(--page) 100%);
    -webkit-mask-image: linear-gradient(90deg, #000 78%, transparent 100%);
            mask-image: linear-gradient(90deg, #000 78%, transparent 100%);
  }
  .quote-sign {
    position: absolute; left: 22px; top: 8px; width: 560px; height: 560px;
    background: var(--sign-white);
    border-left: 6px solid var(--sign-edge);
    border-top: 6px solid #bdbdbd;
    transform: rotate(1.5deg); transform-origin: left top;
  }
  .quote-text {
    position: absolute; left: 58px; top: 44px; width: 560px;
    font: 800 74px/69px "Open Sans", Arial, sans-serif; letter-spacing: -5.5px;
    color: var(--sign-ink); white-space: nowrap;
    transform: rotate(2.5deg); transform-origin: left top;
    -webkit-mask-image: linear-gradient(180deg, #000 70%, rgba(0,0,0,0.25) 100%);
            mask-image: linear-gradient(180deg, #000 70%, rgba(0,0,0,0.25) 100%);
  }
  .quote-text span { display: block; }
  .quote-text .big { font-size: 80px; }
  .quote-fade {
    position: absolute; left: 0; bottom: 0; width: 520px; height: 110px;
    background: linear-gradient(180deg, rgba(239,239,239,0) 0%, rgba(239,239,239,0.85) 100%);
  }
  .quote-credit {
    position: absolute; left: 34px; top: 482px;
    font: italic 15px "Arimo", Arial, sans-serif; color: var(--ink-soft);
  }

  .article-title {
    position: absolute; left: 512px; top: 472px; width: 440px; height: 26px;
    transform: rotate(-90deg); transform-origin: left top;
    font: 700 18.5px "Open Sans", Arial, sans-serif; letter-spacing: 2.2px;
    color: var(--title-grey); white-space: nowrap;
  }
  .article-body {
    position: absolute; left: 590px; top: 24px; width: 482px;
    font-size: 8.6px; line-height: 9.6px; color: var(--ink);
  }
  .article-body p { margin-bottom: 9px; }
  .lower { position: absolute; left: 587px; top: 253px; width: 485px; height: 250px; }
  .health-figure { position: absolute; left: 0; top: 0; width: 210px; }
  .caduceus-photo {
    width: 210px; height: 187px;
    background: radial-gradient(ellipse at 45% 40%, #d7dce5 0%, var(--caduceus-blue) 45%, #dfe2e7 85%, var(--page) 100%);
  }
  .health-figure figcaption {
    margin-top: 4px; padding: 0 8px; text-align: center;
    font: italic 7.4px/9px "Arimo", Arial, sans-serif; color: var(--ink-soft);
  }
  .health-column {
    position: absolute; left: 220px; top: 0; width: 265px;
    font-size: 8.6px; line-height: 9.6px; color: var(--ink);
  }
  .health-column p { margin-bottom: 9px; }
  .page-number {
    position: absolute; left: 1088px; top: 486px; width: 18px; height: 18px; border-radius: 50%;
    background: var(--badge); color: #fff; font: 700 10px/18px "Arimo", Arial, sans-serif; text-align: center;
  }
</style>
</head>
<body>
<main class="spread">
  <div class="quote-wall">
    <div class="quote-sign"></div>
    <blockquote class="quote-text">
      <span>All that is</span>
      <span>necessary for</span>
      <span>evil to triumph</span>
      <span class="big">is that good</span>
      <span class="big">men do</span>
      <span class="big">nothing</span>
    </blockquote>
    <div class="quote-fade"></div>
  </div>
  <p class="quote-credit">- Ambrose Thane</p>

  <h1 class="article-title">VESTED VERMIN FROM A JADE TERRACE</h1>

  <section class="article-body">
    <p>Our society has been specifically structured at every level to achieve control over the entire population of not only a single country, but increasingly the rest of the world. It is all part of the ‘Great Work of Ages’ to impose an all-pervading control system.</p>
    <p>The Brotherhood are experts at wearing different masks despite the single face that is behind them all. Here we are going to look at a number of key sectors of our society in which they have either infiltrated or have effectively controlled from the beginning.</p>
    <p>Writer Dorian Vesk summed up the human experience with this quote:</p>
    <p>‘Just look at us. Everything is backwards; everything is upside down. Doctors destroy health, lawyers destroy justice, universities destroy knowledge, governments destroy freedom, the major media destroy information and religions destroy spirituality’</p>
    <p>He may have added a few more to this list, which I will as it comes along. All of these may seem to be paradoxes and contradictions; but they are not. If you want to impose a planetary prison camp it has to be as Vesk and this novelty describes. To do otherwise would create a world of health, justice, knowledge, freedom, and awareness of true self and reality. Try manipulating the masses in society like that. You can only grasp what is really happening in the world when you understand what the outcome is designed to be, and the pyramid structure we are dealing with.</p>
    <p>This is why Dorian Vesk’s apparent paradoxes are not paradoxes at all. It is the way the world is designed to be. I begin with our health care because it is one of the most sickening of all.</p>
  </section>

  <section class="lower">
    <figure class="health-figure">
      <div class="caduceus-photo" role="img" aria-label="Photo of a chrome winged staff with two entwined serpents beside a red cross badge"></div>
      <figcaption>The international emblem for health depicts two serpents entwined, symbolizing their control over our health system. Symbolism such as this is there for all to see, yet most of us simply don’t see it</figcaption>
    </figure>
    <div class="health-column">
      <p>The medical establishment around the world is just a tool of the pharmaceutical cartel, or ‘Big Pharma’. The last thing it represents is human health. It couldn’t give a care in the world for it. Mainstream medicine is about wealth, not health, and even more than that, it aims to keep from them a connection to their true and infinite self. Big Pharma works as one network, despite the appearance of apparently different ‘companies’, and its classic Illuminati pyramid-within-pyramid structure controls the entire mainstream medical profession and its associated ‘industry’. In truth, it is an ‘industry’ founded on human suffering, and the more suffering the better. After all, healthy people don’t pay medical bills; sick people do. Big Pharma controls what is taught in the medical schools, the drugs that doctors prescribe, how far they can stray from strictly-enforced medical ‘norms’, and dictates government ‘health’ policy.</p>
      <p>It does this through a range of techniques that include political contributions and bribes to doctors such as all-expenses-paid trips to ‘conferences’ in exotic places that are nothing more than free holidays. Mainstream Big Pharma medicine is a grotesque cesspit of corruption and self-interest made even worse by the extraordinary levels of ignorance and incompetence among those who are paid outrageous sums to be ‘medical experts’.</p>
    </div>
  </section>

  <span class="page-number">4</span>
</main>
</body>
</html>
```